Commercial Real Estate Company Needs Website Redesign

Velcaro is a commercial real estate firm that is based in San Diego, but has offices and properties across the U.S. The current website was completed almost 3 years ago and is need of a refresh. We will rework the existing Wordpress CMS system, but require a new design. We have a great programmer who can take the design into wordpress. I need a design template for each page types, There are are approximately 20 pages for each section of our site. There are 4 Sections: Corporate, Hospitality, Commercial/Residential, and Receiver/Bankruptcy. See attached creative brief for the initial pages we would like drafted.

Industry/Entity Type

Real Estate

```html
<!DOCTYPE html>
<html lang="en">
<head>
<meta charset="utf-8">
<title>Velcaro — Commercial Real Estate</title>
<link href="https://fonts.googleapis.com/css2?family=Roboto:ital,wght@0,300;0,400;0,500;0,700;0,900;1,400&family=Roboto+Condensed:wght@700&display=swap" rel="stylesheet">
<style>
:root{
  --navy:#1b2547;
  --navy-deep:#0e1426;
  --footer:#18244a;
  --orange:#f7a12a;
  --orange-band:#f0952a;
  --orange-light:#f6ac45;
  --ink:#1a1a1a;
  --muted:#7c8496;
  --link-blue:#3d5d98;
  --white:#ffffff;
  --soft-white:#c9d0e0;
  --logo-grey:#3f3f3f;
}
*{box-sizing:border-box;margin:0;padding:0}
html,body{width:1025px;height:1200px;overflow:hidden;background:var(--white)}
body{font-family:"Roboto",Arial,sans-serif;color:var(--ink)}
.page{position:relative;width:1025px;height:1200px;overflow:hidden}

/* hero */
.hero{position:absolute;left:0;top:0;width:1025px;height:328px;
  background:linear-gradient(180deg,#5f93c2 0%,#8fb9d9 45%,#a9c6d8 70%,#6d8aa3 100%)}
.site-header{position:absolute;left:60px;top:0;width:908px;height:66px;background:var(--navy);
  clip-path:polygon(0 0,100% 0,94% 100%,6.6% 100%)}
.brand{position:absolute;left:124px;top:15px}
.brand-name{display:block;font-size:24px;font-weight:400;color:var(--white);line-height:1}
.brand-tag{display:block;margin-top:5px;font-size:7px;letter-spacing:1.6px;color:var(--soft-white);text-transform:uppercase}
.main-nav{position:absolute;top:30px;left:0;font-size:11px;color:var(--white)}
.main-nav a{position:absolute;white-space:nowrap;color:var(--white);text-decoration:none}
.main-nav a.active{color:var(--orange)}
.main-nav .caret{position:absolute;left:50%;top:15px;width:5px;height:5px;border-right:1.3px solid currentColor;border-bottom:1.3px solid currentColor;transform:translateX(-50%) rotate(45deg)}
.main-nav .contact-btn{border:1.5px solid var(--orange);padding:4px 7px;top:-6px}
.phone{position:absolute;left:790px;top:17px;color:var(--white);font-size:7.5px;letter-spacing:.3px}
.phone svg{vertical-align:-2px;margin-right:2px}
.phone strong{display:block;color:var(--orange);font-size:10.5px;font-weight:400;margin-top:3px;letter-spacing:.3px}
.social{position:absolute;left:866px;top:20px;height:24px;border-left:1px solid #6c7898;padding-left:6px;display:flex;gap:5px;font-size:8px;color:var(--white);align-items:center}

.slide-caption{position:absolute;left:0;top:278px;width:1025px;height:50px;background:rgba(60,64,70,.72);
  display:flex;align-items:center;justify-content:center;color:var(--white);font-family:"Roboto Condensed",Arial,sans-serif;font-weight:700;font-size:29px}
.slide-arrow{position:absolute;top:290px}

/* dark band */
.services{position:absolute;left:0;top:328px;width:1025px;height:346px;background:var(--navy-deep)}
.newsletter{position:absolute;left:66px;top:328px;width:896px;height:58px;background:var(--orange);
  clip-path:polygon(0 0,100% 0,93.9% 100%,6% 100%)}
.newsletter-label{position:absolute;left:213px;top:349px;font-size:17px;font-weight:300;color:#2a2a2a}
.field{position:absolute;top:345px;height:24px;background:#2b2b2b;color:var(--white);font-style:italic;font-size:11px;padding:5px 6px}
.subscribe-btn{position:absolute;left:701px;top:345px;width:109px;height:24px;border:1.5px solid #1a1a1a;font-size:10.5px;font-weight:700;display:flex;align-items:center;justify-content:center;color:#111}
.service{position:absolute;top:415px;width:236px;text-align:center}
.service h2{font-size:18px;font-weight:300;color:var(--white);margin-bottom:14px}
.service h2 b{font-weight:500}
.service .photo{height:103px;margin-bottom:16px}
.service p{font-size:9.4px;line-height:16px;color:var(--muted)}

/* about */
.about{position:absolute;left:0;top:674px;width:1025px;height:202px;
  background:linear-gradient(135deg,var(--orange-light),var(--orange-band) 55%,#e88d22);
  clip-path:polygon(0 0,100% 0,100% 67%,88% 100%,11.7% 100%,0 67%)}
.about h2{text-align:center;margin-top:16px;font-family:"Roboto Condensed",Arial,sans-serif;font-size:34px;color:var(--white)}
.about p{width:830px;margin:6px auto 0;text-align:center;font-size:14px;line-height:20.5px;color:#2a2113}

/* clients */
.clients h2{position:absolute;left:0;top:895px;width:1025px;text-align:center;font-family:"Roboto Condensed",Arial,sans-serif;font-size:34px;color:var(--navy-deep)}
.client{position:absolute;top:980px;width:170px;height:36px;display:flex;align-items:center;justify-content:center;gap:7px;font-size:22px;font-weight:500;color:var(--logo-grey);white-space:nowrap}
.client-dot{width:26px;height:26px;border-radius:50%;background:var(--logo-grey)}
.client-arrow{position:absolute;top:988px}

/* footer */
.site-footer{position:absolute;left:0;top:1091px;width:1025px;height:109px;background:var(--footer)}
.footer-brand{position:absolute;left:124px;top:1113px}
.address{position:absolute;left:160px;top:1165px;font-size:8.4px;line-height:11px;color:var(--link-blue)}
.footer-nav{position:absolute;right:123px;top:1118px;text-align:right;font-size:8.4px;line-height:11px;color:var(--white)}
.footer-nav .current{color:var(--link-blue);text-decoration:underline}
.copyright{position:absolute;right:123px;top:1165px;font-size:8.4px;letter-spacing:2px;color:var(--link-blue)}
</style>
</head>
<body>
<div class="page">

  <div class="hero" role="img" aria-label="Glass office towers seen from street level against a blue sky"></div>

  <header>
    <div class="site-header"></div>
    <div class="brand"><span class="brand-name">Velcaro</span><span class="brand-tag">Commercial Real Estate</span></div>
    <nav class="main-nav">
      <a class="active" style="left:331px">Who we are<span class="caret"></span></a>
      <a style="left:418px">What we do<span class="caret"></span></a>
      <a style="left:506px">What we've done<span class="caret"></span></a>
      <a class="contact-btn" style="left:611px">Contact us</a>
      <a style="left:702px">Velcaro home</a>
    </nav>
    <div class="phone">
      <svg width="9" height="9" viewBox="0 0 10 10"><path d="M2 0.5 L3.8 2.6 L2.8 3.8 Q4 6.2 6.2 7.2 L7.4 6.2 L9.5 8 L8.3 9.5 Q3.5 9 0.5 1.8 Z" fill="#fff"/></svg>CALL TODAY
      <strong>555-014-2200</strong>
    </div>
    <div class="social"><span>Chirpa</span><span>Netlink</span></div>
  </header>

  <div class="slide-caption">Contact us Today! Let us put our expertise to work for you</div>
  <svg class="slide-arrow" style="left:122px" width="16" height="28" viewBox="0 0 16 28"><path d="M14 2 L3 14 L14 26" fill="none" stroke="#fff" stroke-width="2.5"/></svg>
  <svg class="slide-arrow" style="left:884px" width="16" height="28" viewBox="0 0 16 28"><path d="M2 2 L13 14 L2 26" fill="none" stroke="#fff" stroke-width="2.5"/></svg>

  <section class="services"></section>
  <div class="newsletter"></div>
  <div class="newsletter-label">Subscribe to our newsletter</div>
  <div class="field" style="left:431px;width:128px">Your Name...</div>
  <div class="field" style="left:567px;width:127px">Email Address...</div>
  <div class="subscribe-btn">SUBSCRIBE NOW!</div>

  <article class="service" style="left:120px">
    <h2>For <b>Owners</b></h2>
    <div class="photo" role="img" aria-label="Warm hotel lobby with seating and chandeliers" style="background:linear-gradient(160deg,#c98a3e,#7a4a22 55%,#3b2512)"></div>
    <p>Since 1976, Velcaro has managed full range of hotels, delivering top notch results through a full range of onsite service. From urban city center airport hotels to historic properties to exclusive retreats and resorts.</p>
  </article>
  <article class="service" style="left:392px">
    <h2>For <b>Buyers/Developers</b></h2>
    <div class="photo" role="img" aria-label="Building under construction with cranes against a blue sky" style="background:linear-gradient(180deg,#2f64b8,#6d8fc0 45%,#8a8a86)"></div>
    <p>With Aggressive sales efforts, revenue management expertise, and disciplined expenses controls, Velcaro's operations team is strategically located throughout the country and offers a turnkey approach.</p>
  </article>
  <article class="service" style="left:665px">
    <h2>For <b>Lenders</b></h2>
    <div class="photo" role="img" aria-label="Handshake over a stack of banknotes" style="background:linear-gradient(135deg,#8b6a4c,#d9c5ae 50%,#5a4636)"></div>
    <p>Whether through receivership or REO, Velcaro is able to lenders and special servicers revive distressed and performing hotels and Consistently outperform industry benchmarks.</p>
  </article>

  <section class="about">
    <h2>ABOUT VELCARO</h2>
    <p>Velcaro is a fully integrated commercial real estate management, fiduciary and advisory firm. Leveraging over 38 years of experience in varying economic climates, we provide our clients with outstanding performance and unmatched integrity. We have expertise in the commercial real estate, hospitality and petroleum industries, bringing our broad range of experience and depth of knowledge to every assignment. Whether we are building value through management for investors or solving complex problems for lenders, attorneys and the courts, you can count on Velcaro to maximize value.</p>
  </section>

  <section class="clients">
    <h2>OUR CLIENTS</h2>
    <svg class="client-arrow" style="left:120px" width="21" height="21" viewBox="0 0 21 21"><rect x="1" y="1" width="19" height="19" rx="4" fill="none" stroke="#444" stroke-width="1.5"/><path d="M15 10.5 H6 M9.5 7 L6 10.5 L9.5 14" fill="none" stroke="#444" stroke-width="1.5"/></svg>
    <div class="client" style="left:121px"><span class="client-dot"></span>Halvorn</div>
    <div class="client" style="left:290px">Corvane Bank</div>
    <div class="client" style="left:476px">Meridale</div>
    <div class="client" style="left:674px">Ostrava</div>
    <svg class="client-arrow" style="left:881px" width="21" height="21" viewBox="0 0 21 21"><rect x="1" y="1" width="19" height="19" rx="4" fill="none" stroke="#444" stroke-width="1.5"/><path d="M6 10.5 H15 M11.5 7 L15 10.5 L11.5 14" fill="none" stroke="#444" stroke-width="1.5"/></svg>
  </section>

  <footer class="site-footer"></footer>
  <div class="footer-brand"><span class="brand-name">Velcaro</span><span class="brand-tag">Commercial Real Estate</span></div>
  <div class="address">Velcaro • 4100 Harbor View Drive Suite 210 • San Diego, California 92101<br>Tel: 1.555.014.2200 • Fax: 1.555.014.2300</div>
  <nav class="footer-nav">
    Home &nbsp;|&nbsp; Property Management Receivership &amp; Bankruptcy &nbsp;|<br>
    Lender Conference &nbsp;|&nbsp; Success Stories &nbsp;|&nbsp; <span class="current">About Velcaro</span> &nbsp;|&nbsp; Media Room &nbsp;|<br>
    Contact Us &nbsp;|&nbsp; Careers at Velcaro &nbsp;|&nbsp; Email &nbsp;|&nbsp; Login
  </nav>
  <div class="copyright">© 2013 Velcaro. All Rights Reserved.</div>

</div>
</body>
</html>
```